Braek down, maintainance and support for satelite and TV

I want a website designed for a Orbitline Engineer firm i want it to look modern. I am finalizing the content with the underwriters at the moment so format we can start on the format and pictures. I want it to be easy to navigate with some eye capturing imiges. I am currently waiting for the underwriters to get the contact over so if we can start on everything else. I ONLY ADDED THE SCREEN SHOT AS I HAD TO ADD SOMETHING TO CONTINUE PLEASE USE YOUR OWN IDEAS

Target Market(s)

Every one

Industry/Entity Type

Tv

Number of Pages Required

5+ page

Font styles to use
Sans Serif

```html
<!DOCTYPE html>
<html lang="en">
<head>
<meta charset="utf-8">
<title>Orbitline Engineer – Satellite &amp; TV Breakdown, Maintenance and Support</title>
<link href="https://fonts.googleapis.com/css2?family=Open+Sans:ital,wght@0,400;0,600;0,700;1,400&display=swap" rel="stylesheet">
<style>
  :root{
    --brand-blue:#0aa6d3;
    --link-blue:#3b78b5;
    --steel-blue:#6b96c1;
    --icon-blue:#5b89b9;
    --ink:#222;
    --nav-ink:#3a3a3a;
    --body-ink:#555;
    --panel-grey:#e9e9e9;
    --field-grey:#ececec;
    --footer-bg:#333538;
    --footer-rule:#4a4c50;
    --orange-1:#e9640a;
    --orange-2:#ed7510;
    --orange-3:#f0871a;
    --orange-4:#f49b2c;
    --white:#fff;
  }
  *{box-sizing:border-box;margin:0;padding:0}
  html,body{width:1200px;height:2384px;overflow:hidden}
  body{position:relative;background:var(--white);font-family:"Open Sans",Arial,sans-serif;color:var(--ink)}
  .abs{position:absolute}

  /* Header */
  .site-header{position:absolute;left:0;top:0;width:1200px;height:103px;background:var(--white)}
  .brand-box{position:absolute;left:0;top:0;width:254px;height:103px;background:var(--brand-blue);
    display:flex;flex-direction:column;justify-content:center;padding-left:74px}
  .brand-name{color:var(--white);font-weight:700;font-size:31px;line-height:30px;text-transform:uppercase;letter-spacing:-0.5px}
  .main-nav a{position:absolute;top:57px;font-size:15px;font-weight:600;color:var(--nav-ink);text-decoration:none;text-transform:uppercase}
  .social-dot{position:absolute;width:24px;height:24px;border-radius:50%;background:#b5b5b5}
  .help-text{position:absolute;left:944px;top:43px;font-size:15px;color:#444}
  .help-phone{position:absolute;left:944px;top:60px;font-size:24px;font-weight:700;color:var(--ink)}

  /* Hero */
  .hero{position:absolute;left:0;top:103px;width:1200px;height:571px;
    background:linear-gradient(180deg,#5e5560 0%,#8c6a5c 30%,#c68750 55%,#a9714a 75%,#4c4636 92%,#3c4030 100%)}
  .hero-title{position:absolute;left:74px;top:205px;color:var(--white);font-size:38px;font-weight:700}
  .hero-sub{position:absolute;left:74px;top:251px;color:var(--white);font-size:28px;font-weight:400}
  .feature-tab{position:absolute;top:488px;height:83px;color:var(--white);font-size:23px;font-weight:600;line-height:24px;
    text-transform:uppercase;padding:18px 0 0 28px}
  .slider-dot{position:absolute;top:539px;width:16px;height:16px;border-radius:50%;background:#cfcfcf}
  .slider-dot.is-active{background:var(--white)}

  /* Intro */
  .section-title{position:absolute;font-size:22px;font-weight:600;text-transform:uppercase;color:var(--ink)}
  .title-rule{position:absolute;width:48px;height:2px;background:var(--brand-blue)}
  .intro-text{position:absolute;width:518px;font-size:13.4px;line-height:26px;color:var(--body-ink)}
  .read-more{position:absolute;font-size:13px;font-weight:700;color:var(--link-blue);text-transform:uppercase}

  /* Services */
  .services{position:absolute;left:0;top:1004px;width:1200px;height:332px;background:var(--steel-blue)}
  .services-title{position:absolute;left:0;width:1200px;top:42px;text-align:center;color:var(--white);font-size:22px;font-weight:600;text-transform:uppercase}
  .service-circle{position:absolute;top:101px;width:130px;height:130px;border-radius:50%;background:var(--white);
    display:flex;align-items:center;justify-content:center}
  .service-label{position:absolute;top:243px;width:200px;text-align:center;color:var(--white);font-size:17px;font-weight:700;line-height:21px}

  /* Testimonial */
  .testimonial{position:absolute;left:73px;top:1366px;width:423px;height:401px;background:var(--panel-grey);border-radius:4px}
  .testimonial-title{position:absolute;left:20px;top:20px;font-size:23px;font-weight:600;text-transform:uppercase}
  .testimonial-quote{position:absolute;left:20px;top:73px;width:385px;font-size:13.4px;line-height:24px;font-style:italic;color:var(--body-ink)}
  .testimonial-name{position:absolute;left:20px;top:325px;font-size:14px;font-weight:700;text-transform:uppercase;color:#333}

  /* Video */
  .video-title{position:absolute;left:542px;width:567px;top:1388px;text-align:center;font-size:23px;font-weight:600;text-transform:uppercase}
  .video-frame{position:absolute;left:542px;top:1435px;width:567px;height:332px;border:9px solid var(--brand-blue);
    background:linear-gradient(180deg,#ffffff 0%,#e4e4e4 55%,#c9c9c9 100%)}
  .video-brand{position:absolute;left:0;width:549px;top:80px;text-align:center;color:var(--brand-blue);font-size:34px;font-weight:700;line-height:30px;text-transform:uppercase}
  .play-now{position:absolute;left:315px;top:235px;font-size:15px;font-style:italic;color:var(--brand-blue)}

  /* Footer */
  .site-footer{position:absolute;left:0;top:1811px;width:1200px;height:573px;background:var(--footer-bg);color:var(--white)}
  .footer-heading{position:absolute;left:73px;top:50px;font-size:22px;font-weight:700;text-transform:uppercase}
  .contact-label{position:absolute;left:135px;font-size:13px;font-weight:700;text-transform:uppercase}
  .contact-value{position:absolute;left:135px;font-size:13px;line-height:22px}
  .contact-icon{position:absolute;left:73px}
  .form-label{position:absolute;left:432px;top:117px;font-size:13px;font-weight:700;text-transform:uppercase}
  .form-field{position:absolute;background:var(--field-grey);color:#555;font-size:13px;padding:10px 12px}
  .submit-btn{position:absolute;left:432px;top:318px;width:100px;height:38px;background:var(--brand-blue);color:var(--white);
    font-size:13px;font-weight:600;text-transform:uppercase;display:flex;align-items:center;justify-content:center}
  .footer-brand{position:absolute;left:70px;top:403px;font-size:34px;font-weight:700;line-height:29px;text-transform:uppercase}
  .footer-nav a{position:absolute;top:487px;font-size:13px;color:var(--white);text-decoration:none;text-transform:uppercase}
  .follow-label{position:absolute;left:944px;top:485px;font-size:13px;font-weight:700;text-transform:uppercase}
  .footer-social{position:absolute;top:484px;width:20px;height:20px;border-radius:50%;background:var(--white)}
  .footer-rule{position:absolute;left:73px;top:520px;width:1054px;height:1px;background:var(--footer-rule)}
  .copyright{position:absolute;left:73px;top:536px;font-size:13px}
</style>
</head>
<body>

<header class="site-header">
  <div class="brand-box"><span class="brand-name">Orbitline<br>Engineer</span></div>
  <nav class="main-nav">
    <a style="left:377px">Home</a>
    <a style="left:453px">About Us</a>
    <a style="left:558px">Services</a>
    <a style="left:655px">News</a>
    <a style="left:729px">Contact Us</a>
  </nav>
  <span class="social-dot" style="left:1015px;top:10px"></span>
  <span class="social-dot" style="left:1050px;top:10px"></span>
  <span class="social-dot" style="left:1085px;top:10px"></span>
  <div class="help-text">Need help? Contact US!</div>
  <div class="help-phone">1-000-000-0000</div>
</header>

<section class="hero" role="img" aria-label="Photo of large satellite dishes at a ground station under a sunset sky">
  <h1 class="hero-title">Lorem ipsum dolor sit amet,</h1>
  <p class="hero-sub">consectetur adipiscing elit</p>
  <div class="feature-tab" style="left:73px;width:186px;background:var(--orange-1)">Local<br>Engineers</div>
  <div class="feature-tab" style="left:259px;width:175px;background:var(--orange-2)">Same Day<br>Services</div>
  <div class="feature-tab" style="left:434px;width:175px;background:var(--orange-3)">Free<br>Estimates</div>
  <div class="feature-tab" style="left:609px;width:187px;background:var(--orange-4)">No Hidden<br>Charges</div>
  <span class="slider-dot is-active" style="left:1066px"></span>
  <span class="slider-dot" style="left:1087px"></span>
  <span class="slider-dot" style="left:1107px"></span>
</section>

<section class="intro">
  <h2 class="section-title" style="left:73px;top:713px">Welcome to Orbitline Engineer</h2>
  <span class="title-rule" style="left:73px;top:746px"></span>
  <p class="intro-text" style="left:73px;top:756px">Lorem ipsum dolor sit amet, consectetur adipiscing elit, sed do eiusmod tempor incididunt ut labore et dolore magna aliqua. Ut enim ad minim veniam, quis nostrud exercitation ullamco laboris nisi ut aliquip ex ea commodo consequat. Duis aute irure dolor in reprehenderit in voluptate velit esse cillum dolore eu fugiat nulla pariatur. Excepteur sint occaecat cupidatat non proident, sunt in culpa qui officia deserunt mollit anim id est laborum.</p>
  <span class="read-more" style="left:73px;top:935px">Read More</span>
  <span class="title-rule" style="left:73px;top:956px;width:22px"></span>

  <h2 class="section-title" style="left:615px;top:713px">Who We Are</h2>
  <span class="title-rule" style="left:615px;top:746px"></span>
  <p class="intro-text" style="left:615px;top:756px">Lorem ipsum dolor sit amet, consectetur adipiscing elit, sed do eiusmod tempor incididunt ut labore et dolore magna aliqua. Ut enim ad minim veniam, quis nostrud exercitation ullamco laboris nisi ut aliquip ex ea commodo consequat. Duis aute irure dolor in reprehenderit in voluptate velit esse cillum dolore eu fugiat nulla pariatur. Excepteur sint occaecat cupidatat non proident, sunt in culpa qui officia deserunt mollit anim id est laborum.</p>
  <span class="read-more" style="left:615px;top:935px">Read More</span>
  <span class="title-rule" style="left:615px;top:956px;width:22px"></span>
</section>

<section class="services">
  <h2 class="services-title">Our Services</h2>

  <div class="service-circle" style="left:186px">
    <svg width="44" height="44" viewBox="0 0 44 44" fill="var(--icon-blue)"><circle cx="20" cy="11" r="8" fill="none" stroke="var(--icon-blue)" stroke-width="2.5"/><rect x="17" y="9" width="6" height="20" rx="3"/><path d="M14 24h20v10a6 6 0 0 1-6 6h-8a6 6 0 0 1-6-6z"/></svg>
  </div>
  <div class="service-label" style="left:151px">Switch to<br>Digital</div>

  <div class="service-circle" style="left:418px">
    <svg width="44" height="44" viewBox="0 0 44 44"><g fill="var(--icon-blue)"><circle cx="22" cy="22" r="13"/><rect x="19" y="3" width="6" height="38" rx="1"/><rect x="3" y="19" width="38" height="6" rx="1"/><rect x="19" y="3" width="6" height="38" rx="1" transform="rotate(45 22 22)"/><rect x="19" y="3" width="6" height="38" rx="1" transform="rotate(-45 22 22)"/></g><circle cx="22" cy="22" r="6" fill="#fff"/></svg>
  </div>
  <div class="service-label" style="left:383px">Service and<br>Repairs</div>

  <div class="service-circle" style="left:652px">
    <svg width="48" height="48" viewBox="0 0 48 48" fill="none" stroke="var(--icon-blue)" stroke-width="3" stroke-linecap="round"><path d="M24 5a19 19 0 1 1-17 10"/><path d="M24 14v11l7 5"/><path d="M7 8v7h7"/></svg>
  </div>
  <div class="service-label" style="left:617px">Same Day<br>Service</div>

  <div class="service-circle" style="left:884px">
    <svg width="44" height="44" viewBox="0 0 44 44"><path d="M22 3l16 6v11c0 10-7 18-16 21C13 38 6 30 6 20V9z" fill="var(--icon-blue)"/><path d="M15 22l5 5 9-10" fill="none" stroke="#fff" stroke-width="3.5" stroke-linecap="round" stroke-linejoin="round"/></svg>
  </div>
  <div class="service-label" style="left:849px">Work<br>Guaranteed</div>
</section>

<section class="testimonial">
  <h2 class="testimonial-title">Testimonial</h2>
  <p class="testimonial-quote">“Lorem ipsum dolor sit amet, consectetur adipiscing elit, sed do eiusmod tempor incididunt ut labore et dolore magna aliqua. Ut enim ad minim veniam, quis nostrud exercitation ullamco laboris nisi ut aliquip ex ea commodo consequat. Duis aute irure dolor in reprehenderit in voluptate velit esse cillum dolore eu fugiat nulla pariatur. Excepteur sint occaecat cupidatat non proident, sunt in culpa qui officia deserunt mollit anim id est laborum. Excepteur sint occaecat cupidatat non proident, sunt in culpa qui officia deserunt mollit anim id est laborum.”</p>
  <div class="testimonial-name">-Daniel Harlow</div>
  <svg class="abs" style="left:22px;top:361px" width="34" height="16" viewBox="0 0 34 16" fill="none" stroke="#888" stroke-width="3" stroke-linecap="round" stroke-linejoin="round"><path d="M10 2L4 8l6 6"/><path d="M22 2l6 6-6 6"/></svg>
</section>

<h2 class="video-title">Whtch Our Video</h2>
<div class="video-frame" role="img" aria-label="Video player showing the company name with a play button">
  <div class="video-brand">Orbitline<br>Engineer</div>
  <svg class="abs" style="left:188px;top:226px" width="125" height="56" viewBox="0 0 125 56"><circle cx="28" cy="28" r="25" fill="none" stroke="var(--brand-blue)" stroke-width="4"/><path d="M21 16l20 12-20 12z" fill="var(--brand-blue)"/><line x1="53" y1="28" x2="125" y2="28" stroke="var(--brand-blue)" stroke-width="1.5"/></svg>
  <span class="play-now">Play now</span>
</div>

<footer class="site-footer">
  <h2 class="footer-heading">Get in Touch Now!</h2>

  <svg class="contact-icon" style="top:120px" width="28" height="30" viewBox="0 0 28 30"><path d="M14 2a9 9 0 0 0-9 9c0 7 9 17 9 17s9-10 9-17a9 9 0 0 0-9-9z" fill="var(--brand-blue)"/><circle cx="14" cy="11" r="3.5" fill="var(--footer-bg)"/></svg>
  <div class="contact-label" style="top:120px">Address</div>
  <div class="contact-value" style="top:145px">228, Lorem Ipsum dolor sit,<br>Dosis amet sit - 85485</div>

  <svg class="contact-icon" style="top:216px" width="26" height="26" viewBox="0 0 26 26"><path d="M6 2l5 1 2 6-3 2c1 3 3 5 6 6l2-3 6 2 1 5-3 3C12 24 2 14 3 5z" fill="var(--brand-blue)"/></svg>
  <div class="contact-label" style="top:217px">Phone</div>
  <div class="contact-value" style="top:245px">1-000-000-0000</div>

  <svg class="contact-icon" style="top:310px" width="30" height="22" viewBox="0 0 30 22"><rect x="1" y="1" width="28" height="20" rx="2" fill="var(--brand-blue)"/><path d="M1 3l14 10 14-10" fill="none" stroke="var(--footer-bg)" stroke-width="2.5"/></svg>
  <div class="contact-label" style="top:308px">Email</div>
  <div class="contact-value" style="top:336px">info@orbitlineengineer.com</div>

  <div class="form-label">Leave a Message</div>
  <div class="form-field" style="left:432px;top:151px;width:212px;height:37px">Name</div>
  <div class="form-field" style="left:653px;top:151px;width:221px;height:37px">Email</div>
  <div class="form-field" style="left:883px;top:151px;width:221px;height:37px">Subject</div>
  <div class="form-field" style="left:432px;top:197px;width:672px;height:112px">Message</div>
  <div class="submit-btn">Submit</div>

  <div class="footer-brand">Orbitline<br>Engineer</div>
  <nav class="footer-nav">
    <a style="left:73px">Home</a>
    <a style="left:141px">About Us</a>
    <a style="left:234px">Services</a>
    <a style="left:321px">News</a>
    <a style="left:388px">Contact Us</a>
  </nav>
  <div class="follow-label">Follow Us</div>
  <span class="footer-social" style="left:1036px"></span>
  <span class="footer-social" style="left:1069px"></span>
  <span class="footer-social" style="left:1102px"></span>
  <div class="footer-rule"></div>
  <div class="copyright">©2016 Orbitline Engineer. All Rights Reserved.</div>
</footer>

</body>
</html>
```